2 Business Card Designs

Need two business cards designed:
1) for lumora studio (wedding video) website is lumorastudio.com.au
2) for lumora studio (corporate video) website is lumorastudio.net.au

I am looking for something simple, no fancy shapes etc. Just elegant, simple and classy.

Both companies are video companies, one specialising in weddings the other corporate videos. Neither card needs to have any pics of video or camera related images. Please use same colour schemes as respective websites.

Logo is the same but can change colour.

Industry/Entity Type

Camera

Requirements
Must have
• Logo should be either all white or a colour to match websites
Should not have
• swirls, flowers, shapes, etc.

```html
<!DOCTYPE html>
<html lang="en">
<head>
<meta charset="utf-8">
<title>Lumora Studio – Business Cards</title>
<link href="https://fonts.googleapis.com/css2?family=Quicksand:wght@300;400&family=Open+Sans:wght@400&display=swap" rel="stylesheet">
<style>
  :root {
    --canvas: #000000;
    --olive: #6a6b5b;
    --cream: #dfe3c6;
    --slate-dark: #2f3d47;
    --slate-mid: #3f515c;
    --slate-light: #50646f;
    --slate-band: #8ea2ac;
    --white: #ffffff;
  }
  * { margin: 0; padding: 0; box-sizing: border-box; }
  html, body {
    width: 1200px;
    height: 698px;
    overflow: hidden;
    background: var(--canvas);
  }
  .sheet {
    position: relative;
    width: 1200px;
    height: 698px;
  }
  .card {
    position: absolute;
    overflow: hidden;
  }
  .card--wedding-front { left: 110px; top: 38px; width: 454px; height: 283px; background: var(--cream); }
  .card--wedding-back  { left: 646px; top: 38px; width: 512px; height: 283px; background: var(--olive); }
  .card--corporate-front { left: 110px; top: 379px; width: 454px; height: 283px; }
  .card--corporate-back  { left: 646px; top: 379px; width: 512px; height: 283px; }

  .top-band {
    position: absolute;
    left: 0; top: 0;
    width: 100%; height: 44px;
    background: var(--olive);
  }
  .frame-strip {
    position: absolute;
    display: flex;
    gap: 14px;
  }
  .frame-strip--vertical {
    right: 14px; top: 72px;
    flex-direction: column;
  }
  .frame-strip--horizontal {
    left: 24px; top: 248px;
    gap: 17.6px;
  }
  .frame {
    width: 22px; height: 22px;
  }
  .frame-strip--vertical .frame { background: var(--olive); }
  .frame-strip--horizontal .frame { background: var(--cream); }

  .brushed-texture {
    position: absolute;
    inset: 0;
    background: linear-gradient(90deg,
      var(--slate-dark) 0%, var(--slate-mid) 8%, var(--slate-dark) 15%,
      var(--slate-light) 24%, var(--slate-mid) 32%, var(--slate-dark) 40%,
      var(--slate-mid) 50%, var(--slate-light) 60%, var(--slate-dark) 68%,
      var(--slate-mid) 78%, var(--slate-light) 86%, var(--slate-dark) 94%,
      var(--slate-mid) 100%);
  }

  .wordmark {
    position: absolute;
    left: 20px;
    top: 40px;
    width: 350px;
    text-align: center;
    font-family: "Quicksand", sans-serif;
    font-weight: 300;
  }
  .wordmark__name {
    display: block;
    font-size: 96px;
    line-height: 1;
    letter-spacing: 1px;
  }
  .wordmark__line {
    display: block;
    margin-top: 6px;
    font-size: 26px;
    line-height: 1;
    letter-spacing: 0.55em;
    padding-left: 0.55em;
  }
  .card--wedding-front .wordmark { color: var(--olive); }
  .card--corporate-front .wordmark { color: var(--white); top: 22px; }

  .web-address {
    position: absolute;
    font-family: "Open Sans", sans-serif;
    font-size: 22px;
    line-height: 1;
  }
  .card--wedding-front .web-address {
    left: 26px; top: 213px;
    color: var(--olive);
  }
  .address-band {
    position: absolute;
    left: 0; bottom: 0;
    width: 100%; height: 59px;
    background: var(--slate-band);
  }
  .card--corporate-front .web-address {
    left: 28px; top: 18px;
    color: var(--white);
  }
</style>
</head>
<body>
<main class="sheet">

  <section class="card card--wedding-front">
    <div class="top-band"></div>
    <div class="wordmark">
      <span class="wordmark__name">lumora</span>
      <span class="wordmark__line">STUDIO</span>
    </div>
    <p class="web-address">www.LumoraStudio.com.au</p>
    <div class="frame-strip frame-strip--vertical">
      <span class="frame"></span><span class="frame"></span><span class="frame"></span>
      <span class="frame"></span><span class="frame"></span><span class="frame"></span>
    </div>
  </section>

  <section class="card card--wedding-back">
    <div class="frame-strip frame-strip--horizontal">
      <span class="frame"></span><span class="frame"></span><span class="frame"></span>
      <span class="frame"></span><span class="frame"></span><span class="frame"></span>
      <span class="frame"></span><span class="frame"></span><span class="frame"></span>
      <span class="frame"></span><span class="frame"></span><span class="frame"></span>
    </div>
  </section>

  <section class="card card--corporate-front">
    <div class="brushed-texture" role="img" aria-label="Brushed slate-blue vertical streak texture"></div>
    <div class="wordmark">
      <span class="wordmark__name">lumora</span>
      <span class="wordmark__line">STUDIO</span>
    </div>
    <div class="address-band">
      <p class="web-address">www.LumoraStudio.net.au</p>
    </div>
  </section>

  <section class="card card--corporate-back">
    <div class="brushed-texture" role="img" aria-label="Brushed slate-blue vertical streak texture"></div>
  </section>

</main>
</body>
</html>
```